Price Comparison Homepage

We are a price comparison service. I would like a concept page for a new homepage for our financial comparison service. Current homepage can be found at www.coinlantern.com.hk/en

I have also attached another concept which includes the sample content we
would like to include on the concept...

Note: The footer area (from "why choose coinlantern" down) is fixes as is
the header (menu).

The new colours are shown in the attachment, we are moving away from the
green and to the blue attached.

Financial

```html
<!DOCTYPE html>
<html lang="en">
<head>
<meta charset="utf-8">
<title>CoinLantern – Compare Credit Cards, Loans and Insurance</title>
<link href="https://fonts.googleapis.com/css2?family=Open+Sans:wght@300;400;600;700&display=swap" rel="stylesheet">
<style>
:root{
  --sky:#74a7e6;
  --sky-light:#8ab6ec;
  --nav:#6f9fdc;
  --navy:#1b2f8f;
  --band:#3d4d7e;
  --tan:#a08a60;
  --bronze:#b07a3a;
  --green:#6fa843;
  --green-text:#1f9a3a;
  --brand:#1f3f9a;
  --orange:#c0661f;
  --white:#ffffff;
  --ink:#111111;
}
*{margin:0;padding:0;box-sizing:border-box}
html,body{width:1200px;height:2264px;overflow:hidden}
body{font-family:"Open Sans",Arial,sans-serif;color:var(--white);background:var(--sky);position:relative}
.abs{position:absolute}

.site-header{left:0;top:0;width:1200px;height:113px;background:var(--sky)}
.brand{left:26px;top:30px;display:flex;align-items:center;gap:12px}
.brand-mark{width:44px;height:44px;border-radius:50%;background:var(--brand)}
.brand-name{font-size:44px;font-weight:700;color:var(--brand);line-height:1}
.helpline{left:748px;top:24px;color:var(--ink);font-size:17px}
.helpline strong{display:block;font-size:26px;font-weight:400;color:var(--white)}
.helpline strong small{font-size:15px}

.main-nav{left:0;top:113px;width:1200px;height:110px;background:var(--nav);display:flex}
.main-nav a{width:171px;height:110px;display:flex;align-items:center;justify-content:center;text-align:center;
  color:#e6efff;text-decoration:none;font-size:15px;text-transform:uppercase;border-right:1px solid rgba(255,255,255,.25);line-height:1.2}
.main-nav a:last-child{border-right:0}

.hero{left:0;top:223px;width:1200px;height:556px;background:var(--sky)}
.hero-photo{left:0;top:0;width:440px;height:556px;background:linear-gradient(180deg,#8fb6ea 0%,#5d7fb0 55%,#2a3346 100%)}
.hero-title{left:560px;top:135px;width:590px;text-align:center;font-size:31px;font-weight:300;line-height:1.3}
.hero-why{left:560px;top:270px;width:590px;text-align:center;font-size:31px;font-weight:300}
.hero-why b{color:var(--brand);font-weight:400}
.features{left:443px;top:343px;width:742px;height:123px;background:rgba(255,255,255,.35);border:2px solid rgba(255,255,255,.45);display:flex;align-items:center;justify-content:space-around}
.feature{display:flex;align-items:center;gap:14px;color:#4a6fae;font-size:16px;line-height:1.4}

.search-band{left:0;top:779px;width:1200px;height:221px;background:var(--band)}
.tabs{left:104px;top:13px;display:flex}
.tab{width:227px;height:38px;background:var(--tan);color:#1d2c5a;font-size:12px;font-weight:600;display:flex;align-items:center;gap:10px;padding-left:18px;border-right:2px solid var(--band)}
.tab.is-active{background:#dfe6f5;color:#2e8a36}
.search-title{left:217px;top:62px;font-size:32px;font-weight:600}
.search-sub{left:217px;top:100px;font-size:13px;font-weight:600}
.select{top:146px;height:37px;background:var(--white);color:#888;font-size:12px;display:flex;align-items:center;justify-content:space-between;padding:0 22px 0 32px;border-radius:2px}
.select::after{content:"";border:7px solid transparent;border-top:8px solid #555;margin-top:8px}
.btn-compare{left:692px;top:146px;width:163px;height:37px;background:var(--bronze);color:var(--ink);font-weight:700;font-size:15px;display:flex;align-items:center;justify-content:center}
.need-help{left:881px;top:157px;font-size:13px}

.company{left:0;top:1000px;width:1200px;height:194px;background:var(--sky);text-align:center}
.company h2{margin-top:20px;font-size:30px;font-weight:700}
.company p{width:880px;margin:12px auto 0;font-size:13px;line-height:1.85;color:#dbe8fb}

.steps{left:0;top:1194px;width:1200px;height:349px;background:var(--sky-light)}
.steps h2{position:absolute;left:0;top:24px;width:1200px;text-align:center;font-size:22px;font-weight:600;color:#2f3d6b}
.steps h2 em{font-style:normal;color:var(--green-text)}
.step{top:102px;width:220px;text-align:center}
.step h3{font-size:18px;font-weight:700;color:#2f3d6b;text-transform:uppercase}
.step-circle{width:150px;height:150px;border-radius:50%;background:var(--green);margin:10px auto 0;display:flex;align-items:center;justify-content:center}
.step p{margin-top:10px;color:var(--orange);font-size:13px;line-height:1.6}

.news{left:0;top:1543px;width:1200px;height:340px;background:var(--sky)}
.rule{height:2px;background:var(--green)}
.news h2{left:40px;top:44px;font-size:22px;font-weight:400}
.news h2 b{color:var(--brand);font-weight:600}
.news-item{left:38px;width:600px;display:flex;gap:14px}
.news-icon{width:82px;height:85px;flex:none;display:flex;align-items:center;justify-content:center}
.news-item h3{color:var(--ink);font-size:17px;font-weight:400;margin-top:-4px}
.news-item p{font-size:12px;font-weight:600;line-height:1.55;margin-top:4px}
.partner{width:180px;height:44px;background:rgba(255,255,255,.35);border-radius:6px}

.site-footer{left:0;top:1883px;width:1200px;height:312px;background:var(--navy)}
.foot-col{top:42px;font-size:12.5px;line-height:1.45;color:#dfe6ff}
.foot-col h4{color:#8ec94e;font-size:17px;font-weight:400;margin-bottom:14px}
.testimonial{left:26px;top:188px;width:620px}
.testimonial h4{font-size:18px;font-weight:600}
.testimonial p{margin-top:12px;color:#e3a23a;font-size:11.5px;line-height:1.65}
.connect{left:825px;top:195px}
.connect h4{color:#8ec94e;font-size:18px;font-weight:400}
.socials{display:flex;gap:14px;margin-top:18px}
.socials span{width:26px;height:26px;border-radius:50%;background:#8a93ad}

.promise{left:0;top:2195px;width:1200px;height:32px;background:#3c6fc7;font-size:12px;font-weight:700;color:#b7d78e;letter-spacing:.5px}
.promise span{position:absolute;top:8px}
.legal{left:0;top:2227px;width:1200px;height:37px;background:var(--green);color:#1b2f5f;font-size:12px;display:flex;align-items:center;justify-content:center}
</style>
</head>
<body>

<header class="site-header abs">
  <div class="brand abs"><span class="brand-mark"></span><span class="brand-name">CoinLantern</span></div>
  <div class="helpline abs">Call now for assistance:<strong>2345 6789<small>(Mon - Fri, 9am - 7pm)</small></strong></div>
</header>

<nav class="main-nav abs">
  <a href="#" aria-label="Home"><svg width="40" height="34" viewBox="0 0 40 34"><path d="M20 2 2 18h5v14h10v-9h6v9h10V18h5z" fill="#4a5f82"/></svg></a>
  <a href="#">About<br>Coin Lantern</a>
  <a href="#">Credit Card</a>
  <a href="#">Personal Loans</a>
  <a href="#">Mortgage</a>
  <a href="#">Travel<br>Insurance</a>
  <a href="#">Health<br>Insurance</a>
</nav>

<section class="hero abs">
  <div class="hero-photo abs" role="img" aria-label="Photograph of two smiling business people in suits, one holding a folder, one gesturing toward the headline"></div>
  <h1 class="hero-title abs">The Best way to compare<br>Credit Card, Loan and Insurance.</h1>
  <p class="hero-why abs">Why Choose <b>CoinLantern</b>?</p>
  <div class="features abs">
    <div class="feature"><svg width="56" height="56" viewBox="0 0 56 56"><path d="M8 30 30 8h18v18L26 48z" fill="none" stroke="#4a6fae" stroke-width="4"/><circle cx="40" cy="16" r="3" fill="#4a6fae"/></svg>100 % free</div>
    <div class="feature"><svg width="70" height="80" viewBox="0 0 70 80"><rect x="4" y="4" width="40" height="52" fill="none" stroke="#4a6fae" stroke-width="3"/><rect x="18" y="16" width="40" height="52" fill="#dbe6f7" stroke="#4a6fae" stroke-width="3"/><path d="M26 30h24M26 38h24M26 46h16" stroke="#4a6fae" stroke-width="3"/><circle cx="44" cy="64" r="12" fill="#4a6fae"/><path d="m38 64 5 5 8-9" stroke="#fff" stroke-width="3" fill="none"/></svg>Compare quickly<br>and easily</div>
    <div class="feature"><svg width="50" height="70" viewBox="0 0 50 70"><path d="M14 40 8 66l17-8 17 8-6-26" fill="#4a6fae"/><circle cx="25" cy="26" r="22" fill="#4a6fae"/><circle cx="25" cy="26" r="15" fill="none" stroke="#dbe6f7" stroke-width="3"/></svg>100% Impartial<br>and independant</div>
  </div>
</section>

<section class="search-band abs">
  <div class="tabs abs">
    <div class="tab is-active"><svg width="34" height="22" viewBox="0 0 34 22"><rect x="1" y="1" width="30" height="19" rx="2" fill="#333"/><rect x="1" y="6" width="30" height="4" fill="#ddd"/></svg>CREDIT CARDS</div>
    <div class="tab"><svg width="28" height="26" viewBox="0 0 28 26"><path d="M9 4h10l-3 5a10 10 0 1 1-4 0z" fill="#222"/></svg>ROLLOVER LOANS</div>
    <div class="tab"><svg width="34" height="24" viewBox="0 0 34 24"><path d="M3 16 8 6h16l5 10v5H3z" fill="#222"/></svg>CAR INSURANCE</div>
    <div class="tab"><svg width="34" height="26" viewBox="0 0 34 26"><path d="M3 10a20 20 0 0 1 28 0M8 15a13 13 0 0 1 18 0M13 20a6 6 0 0 1 8 0" stroke="#222" stroke-width="3" fill="none"/></svg>BROAD BAND</div>
  </div>
  <h2 class="search-title abs">Find your perfect credit card in seconds....</h2>
  <p class="search-sub abs">Apply through us and get online application rewards! 100% free &amp; rewards</p>
  <div class="select abs" style="left:221px;width:207px">Which Banks?</div>
  <div class="select abs" style="left:442px;width:205px">Which cards types ?</div>
  <div class="btn-compare abs">COMPARE NOW</div>
  <div class="need-help abs">Need help?</div>
</section>

<section class="company abs">
  <h2>THE COMPANY</h2>
  <p>Lorem ipsum dolor sit amet, consectetuer adipiscing elit. Praesent vestibulum molestie lacus. Aenean nonummy hendrerit mauris. Phasellus porta. Lorem ipsum dolor sit amet, r adipiscing elit. Praesent vestibulum molestie lacus. Aenean nonummy hendrerit mauris. Phasellus porta. Fusce suscipit varius mi. Cum sociis natoque penatibus et magnis dis parturient montes, nascur ridiculus mus. Nulla dui. Fusce feugiat malesuada odio. Morbi nunc odio.</p>
</section>

<section class="steps abs">
  <h2>Compare then buy in <em>3 easy steps</em></h2>
  <div class="step abs" style="left:167px">
    <h3>Step 1</h3>
    <div class="step-circle"><svg width="70" height="86" viewBox="0 0 70 86"><rect x="4" y="4" width="62" height="78" fill="#fff"/><g fill="#6fa843"><rect x="14" y="18" width="8" height="8"/><rect x="28" y="20" width="28" height="4"/><rect x="14" y="34" width="8" height="8"/><rect x="28" y="36" width="28" height="4"/><rect x="14" y="50" width="8" height="8"/><rect x="28" y="52" width="28" height="4"/><rect x="28" y="66" width="28" height="4"/></g></svg></div>
    <p>Fill in the form<br>to get instant result</p>
  </div>
  <div class="step abs" style="left:445px">
    <h3>Step 2</h3>
    <div class="step-circle"><svg width="80" height="80" viewBox="0 0 80 80"><circle cx="46" cy="32" r="24" fill="none" stroke="#fff" stroke-width="6"/><path d="M28 50 8 72" stroke="#fff" stroke-width="8" stroke-linecap="round"/></svg></div>
    <p>Compare the products</p>
  </div>
  <div class="step abs" style="left:748px">
    <h3>Step 3</h3>
    <div class="step-circle"><svg width="80" height="80" viewBox="0 0 80 80"><path d="M60 40v30H8V18h40" fill="none" stroke="#fff" stroke-width="7"/><path d="m20 38 14 14 36-40" fill="none" stroke="#fff" stroke-width="9"/></svg></div>
    <p>Buy the best option</p>
  </div>
</section>

<section class="news abs">
  <div class="rule abs" style="left:38px;top:26px;width:165px"></div>
  <h2 class="abs">Latest <b>LanternMax</b> news</h2>
  <article class="news-item abs" style="top:80px">
    <div class="news-icon" style="background:#a6c1cf"><svg width="56" height="40" viewBox="0 0 56 40"><g fill="#fff"><circle cx="28" cy="10" r="8"/><path d="M14 40a14 14 0 0 1 28 0z"/><circle cx="11" cy="15" r="6"/><path d="M0 38a11 11 0 0 1 16-10l-2 10z"/><circle cx="45" cy="15" r="6"/><path d="M56 38a11 11 0 0 0-16-10l2 10z"/></g></svg></div>
    <div><h3>Amet consectetuer adipiscing</h3><p>Lorem ipsum dolor sit amet, r adipiscing elit. Praesent vestibulum molestie lacus. Aenean nonummy hendrerit mauris. Phasellus porta. Fusce suscipit varius mi. Cum sociis natoque penatibus et magnis dis parturient montes, nascur ridiculus mus. Nulla dui. Fusce feugiat malesuada odio. Morbi nunc odio.</p></div>
  </article>
  <article class="news-item abs" style="top:202px">
    <div class="news-icon" style="background:#e2431d"><svg width="50" height="40" viewBox="0 0 50 40"><path d="M4 14h10l22-12v36L14 26H4z" fill="#fff"/><path d="M12 26l4 12h6l-3-12z" fill="#fff"/><path d="M42 12v16" stroke="#fff" stroke-width="4"/></svg></div>
    <div><h3>Fusce suscipit varius mi</h3><p>Lorem ipsum dolor sit amet, r adipiscing elit. Praesent vestibulum molestie lacus. Aenean nonummy hendrerit mauris. Phasellus porta. Fusce suscipit varius mi. Cum sociis natoque penatibus et magnis dis parturient montes, nascur ridiculus mus. Nulla dui. Fusce feugiat malesuada odio. Morbi nunc odio.</p></div>
  </article>
  <div class="rule abs" style="left:711px;top:45px;width:160px"></div>
  <div class="partner abs" style="left:711px;top:106px"></div>
  <div class="partner abs" style="left:934px;top:106px"></div>
  <div class="partner abs" style="left:711px;top:182px"></div>
  <div class="partner abs" style="left:934px;top:182px"></div>
  <div class="partner abs" style="left:730px;top:252px;width:150px"></div>
  <div class="partner abs" style="left:940px;top:250px;width:150px"></div>
</section>

<footer class="site-footer abs">
  <div class="foot-col abs" style="left:38px"><h4>CREDIT CARD</h4></div>
  <ul class="foot-col abs" style="left:26px;top:78px;list-style:none"><li>Credit Card Comparison</li><li>Credit Card FAQ</li><li>Credit Card Glossary</li><li>Credit Card Guide</li></ul>
  <div class="foot-col abs" style="left:258px"><h4>LOAN</h4></div>
  <ul class="foot-col abs" style="left:208px;top:78px;list-style:none"><li>Personal Loan Comparison</li><li>Personal Loan Guide</li><li>Mortgage</li></ul>
  <div class="foot-col abs" style="left:443px"><h4>INSURANCE</h4></div>
  <ul class="foot-col abs" style="left:402px;top:78px;list-style:none"><li>Health Insurance Comparison</li><li>Travel Insurance Comparison</li></ul>
  <div class="foot-col abs" style="left:821px;top:30px"><h4>Menu</h4></div>
  <ul class="foot-col abs" style="left:821px;top:66px;list-style:none"><li>About</li><li>Contact Us</li><li>FAQs</li><li>Product Guide</li><li>Careers</li></ul>
  <ul class="foot-col abs" style="left:950px;top:60px;list-style:none"><li>Terms &amp; Conditions and Privacy Policy</li><li>Glossary</li><li>Affiliates</li><li>Press</li><li>Sitemap</li><li>Blog</li></ul>
  <div class="testimonial abs">
    <h4>See what our Customers say!</h4>
    <p>Thanks CoinLantern for helping me choose the right credit card.<br>Not sure I would have avoided all these hidden fees and high interest rates without you.<br>Mandy, Kowloon</p>
  </div>
  <div class="connect abs"><h4>Connect with us</h4><div class="socials"><span></span><span></span><span></span></div></div>
</footer>

<div class="promise abs"><span style="left:148px">INDEPENDENT &amp; IMPARTIAL</span><span style="left:434px">FREE &amp; WITHOUT OBLIGATION</span><span style="left:718px">EASY MARKET COMPARISON</span></div>
<div class="legal abs">© 2013 - 2014 CoinLantern Global Limited. All rights reserved. Use of this site constitutes acceptance of our Terms of Use and Privacy Policy.</div>

</body>
</html>
```